Business card design needed

I need a business card for my new business.
I make environmentally friendly candles from all natural premium ingredients.
The candles are hand-poured locally in Melbourne, Australia.
I also want my card to match my website www.velmoracandles-example.com.au (similar colours, font). Can add additional fonts to create more interest...
I want my design to reflect class and simplicity.
Target Market(s)
Target audience 25-50
The candles represent luxury but need to appeal to the environmentally conscious...
Needs to appeal to both men and women. A luxury gift a man would buy for his girlfriend or mother or for his home and for a woman it needs to represent quality...
Industry/Entity Type
Business
Contact Information for Business Card
Velmora Candles
Hand-Poured Eco Soy Candles
Lorena Whitcombe - Founder
0472 390 614
www.velmoracandles-example.com.au
Logo Text
VELMORA
Logo styles of interest
Wordmark Logo
Look and feel
Each slider illustrates characteristics of the customer's brand and the style your logo design should communicate.

```html
<!DOCTYPE html>
<html lang="en">
<head>
<meta charset="utf-8">
<title>Velmora Candles – Business Card Options</title>
<link rel="stylesheet" href="https://fonts.googleapis.com/css2?family=Arvo:wght@400;700&display=swap">
<style>
  :root {
    --backdrop: #ece7e1;
    --card-blue: #d3ebef;
    --card-white: #ffffff;
    --ink: #2a2a2a;
    --shadow: rgba(40, 25, 15, 0.28);
  }
  * { margin: 0; padding: 0; box-sizing: border-box; }
  html, body {
    width: 1200px;
    height: 739px;
    overflow: hidden;
    background: var(--backdrop);
  }
  body {
    position: relative;
    font-family: "Arvo", "Rockwell", Georgia, serif;
    color: var(--ink);
  }
  .card {
    position: absolute;
    width: 494px;
    height: 284px;
    background: var(--card-blue);
    box-shadow: 0 4px 14px var(--shadow);
    overflow: hidden;
  }
  .card--a { left: 78px; top: 78px; }
  .card--b { left: 627px; top: 78px; }
  .card--c { left: 350px; top: 399px; height: 275px; background: var(--card-white); }

  .band { position: absolute; left: 0; width: 100%; }
  .band--footer-white { top: 241px; bottom: 0; background: var(--card-white); }
  .band--header-blue { top: 0; height: 86px; background: var(--card-blue); }
  .band--footer-blue { top: 238px; bottom: 0; background: var(--card-blue); }

  .line {
    position: absolute;
    left: 0;
    width: 100%;
    text-align: center;
    transform: translateY(-50%);
    white-space: nowrap;
    line-height: 1;
  }
  .brand-name { font-size: 30px; letter-spacing: 5px; }
  .tagline { font-size: 14px; letter-spacing: 3.2px; }
  .card--a .tagline { font-size: 15.5px; letter-spacing: 3.4px; }

  .person {
    display: inline-block;
    text-align: right;
  }
  .person-name { display: block; letter-spacing: 4px; font-size: 23px; }
  .person-role { display: block; letter-spacing: 3px; font-size: 16px; margin-top: 6px; }
  .card--a .person-name { font-size: 26px; letter-spacing: 4.5px; }
  .card--a .person-role { font-size: 18px; margin-top: 7px; }

  .phone {
    font-size: 20px;
    letter-spacing: 3px;
    display: inline-flex;
    align-items: center;
    gap: 3px;
  }
  .phone svg { width: 21px; height: 21px; }
  .website { font-size: 11.5px; letter-spacing: 2.6px; }
</style>
</head>
<body>

  <!-- Option A: tagline-led -->
  <section class="card card--a">
    <div class="band band--footer-white"></div>
    <p class="line tagline" style="top:51px">HAND-POURED ECO SOY CANDLES</p>
    <div class="line" style="top:133px">
      <span class="person">
        <span class="person-name">Lorena Whitcombe</span>
        <span class="person-role">Founder</span>
      </span>
    </div>
    <div class="line" style="top:210px">
      <span class="phone">
        <svg viewBox="0 0 24 24" aria-hidden="true"><circle cx="12" cy="12" r="10.5" fill="none" stroke="currentColor" stroke-width="1.6"/><path d="M8.6 6.4l1.8-.4 1.1 2.8-1.3 1c.6 1.5 1.6 2.6 3 3.3l1-1.3 2.8 1.1-.4 1.9c-.2.5-.7.8-1.3.7-3.7-.6-6.7-3.6-7.3-7.3-.1-.6.2-1.1.6-1.3z" fill="currentColor"/></svg>
        0472 390 614
      </span>
    </div>
    <p class="line website" style="top:255px">www.velmoracandles-example.com.au</p>
  </section>

  <!-- Option B: name-led -->
  <section class="card card--b">
    <div class="band band--footer-white"></div>
    <h1 class="line brand-name" style="top:47px">VELMORA CANDLES</h1>
    <p class="line tagline" style="top:73px">HAND-POURED ECO SOY CANDLES</p>
    <div class="line" style="top:138px">
      <span class="person">
        <span class="person-name">Lorena Whitcombe</span>
        <span class="person-role">Founder</span>
      </span>
    </div>
    <div class="line" style="top:210px">
      <span class="phone">
        <svg viewBox="0 0 24 24" aria-hidden="true"><circle cx="12" cy="12" r="10.5" fill="none" stroke="currentColor" stroke-width="1.6"/><path d="M8.6 6.4l1.8-.4 1.1 2.8-1.3 1c.6 1.5 1.6 2.6 3 3.3l1-1.3 2.8 1.1-.4 1.9c-.2.5-.7.8-1.3.7-3.7-.6-6.7-3.6-7.3-7.3-.1-.6.2-1.1.6-1.3z" fill="currentColor"/></svg>
        0472 390 614
      </span>
    </div>
    <p class="line website" style="top:255px">www.velmoracandles-example.com.au</p>
  </section>

  <!-- Option C: banded -->
  <section class="card card--c">
    <div class="band band--header-blue"></div>
    <div class="band band--footer-blue"></div>
    <h2 class="line brand-name" style="top:38px">VELMORA CANDLES</h2>
    <p class="line tagline" style="top:65px">HAND-POURED ECO SOY CANDLES</p>
    <div class="line" style="top:131px">
      <span class="person">
        <span class="person-name">Lorena Whitcombe</span>
        <span class="person-role">Founder</span>
      </span>
    </div>
    <div class="line" style="top:206px">
      <span class="phone">
        <svg viewBox="0 0 24 24" aria-hidden="true"><circle cx="12" cy="12" r="10.5" fill="none" stroke="currentColor" stroke-width="1.6"/><path d="M8.6 6.4l1.8-.4 1.1 2.8-1.3 1c.6 1.5 1.6 2.6 3 3.3l1-1.3 2.8 1.1-.4 1.9c-.2.5-.7.8-1.3.7-3.7-.6-6.7-3.6-7.3-7.3-.1-.6.2-1.1.6-1.3z" fill="currentColor"/></svg>
        0472 390 614
      </span>
    </div>
    <p class="line website" style="top:254px">www.velmoracandles-example.com.au</p>
  </section>

</body>
</html>
```